High End Personalized Functional Medicine in Women's Health

We are adding new and exciting personalized medicine services to our Women's Health Care practice focusing on health optimization and anti-aging as well as hormone replacement therapy and need a high end brochure to educate patients about these services. We would like to see a zen-like design that has feminine appeal. Our office colors are vibrant but soothing. We have utilized the concepts of feng shui to optimize our positive energy. The exterior of the building is peach and cream and these colors would blend with that energy The final design should communicate a sense that you can take control of your health and aging.

Target Market(s)

Females age 35-65 with annual income >$75000/year

Industry/Entity Type

Health And Wellness

Logo Text

Bright Path is the company name. Our sister company is Corva Ridge Ob/Gyn

Font styles to use
Serif

Colors

Designer to choose colors to be used in the design.

Requirements
Must have
• My project must have clean lines. I like a strong feminine appearance, not a fluffy curvy feminine look. Professional appearance, Brochure would be on thicker card stock. A strong front page that makes you want to open the brochure
Nice to have
• Eye catching photos that complement our message . I am not tied to the peach and cream color recommendation, but find those colors feminine but not so cliche as pinks and purples.
Should not have
• frilly design

```html
<!DOCTYPE html>
<html lang="en">
<head>
<meta charset="utf-8">
<title>Bright Path Functional Medicine – Trifold Brochure</title>
<link href="https://fonts.googleapis.com/css2?family=Lato:ital,wght@0,300;0,400;1,300&display=swap" rel="stylesheet">
<style>
:root{
  --bg:#d9d9d9;
  --paper:#ffffff;
  --rose:#d3aca5;
  --rose-soft:#e4cfcb;
  --rose-deep:#bf8a80;
  --rose-text:#c4897e;
  --ink:#555050;
  --ink-soft:#6d6666;
  --white:#ffffff;
}
*{margin:0;padding:0;box-sizing:border-box}
html,body{width:789px;height:1200px;overflow:hidden;background:var(--bg)}
body{font-family:"Lato",sans-serif;font-weight:300;color:var(--ink);position:relative}
.spread{position:absolute;left:67px;width:654px;height:507px;display:flex;box-shadow:0 14px 14px -10px rgba(0,0,0,.35)}
.spread--outside{top:59px}
.spread--inside{top:605px}
.panel{position:relative;width:218px;height:507px;background:var(--paper);overflow:hidden}
.panel--rose{background:linear-gradient(180deg,#e2cdca 0%,#d6b7b2 100%)}
.panel--solid{background:var(--rose)}
.footer-band{position:absolute;left:0;right:0;bottom:0;height:29px;background:var(--rose);color:var(--white);
  font-size:12px;display:flex;align-items:center;justify-content:center;gap:6px;letter-spacing:.2px}
.footer-band--overlay{background:rgba(211,172,165,.85)}
.footer-band svg{width:10px;height:10px}
.photo{position:absolute;left:0;width:100%}
.lead{position:absolute;left:11px;right:9px;color:var(--rose-text);font-size:9.6px;line-height:1.33}
.body{position:absolute;left:11px;right:9px;font-size:6.1px;line-height:1.42;text-align:justify;color:var(--ink-soft)}
.body p+p{margin-top:7px}
.heading{position:absolute;left:11px;right:9px;color:var(--rose-text);font-size:10px;line-height:1.3}
.heading--rule{border-bottom:.6px solid var(--rose-text);padding-bottom:2px;right:auto}
/* testimonial panel */
.portrait-ring{position:absolute;left:50%;top:26px;transform:translateX(-50%);width:118px;height:118px;border-radius:50%;
  background:var(--paper);padding:3px;box-shadow:0 0 0 2px rgba(255,255,255,.35)}
.portrait-ring div{width:100%;height:100%;border-radius:50%;background:linear-gradient(160deg,#a9b49a,#6f7f5e 60%,#c9bfae)}
.testimonial-title{position:absolute;left:0;right:0;top:164px;text-align:center;font-size:10.2px;line-height:1.55;color:var(--ink)}
.quote-mark{position:absolute;left:0;right:0;text-align:center;color:var(--rose-deep);font-size:24px;line-height:1;font-weight:400}
.quote{position:absolute;left:13px;right:13px;font-style:italic;font-size:6.4px;line-height:1.75;color:#b5857d}
.contact{position:absolute;left:0;right:0;top:386px;text-align:center;font-size:7.6px;line-height:1.8;color:var(--ink)}
.social{position:absolute;left:0;right:0;top:449px;display:flex;justify-content:center;gap:12px}
.social span{width:15px;height:15px;border:1px solid var(--rose-deep);border-radius:50%}
/* cover */
.brand{position:absolute;left:0;right:0;top:36px;text-align:center;color:var(--ink)}
.brand-dot{width:22px;height:22px;border:1.2px solid var(--rose-deep);border-radius:50%;margin:0 auto 12px}
.brand-name{font-size:11px;letter-spacing:8px;padding-left:8px;font-weight:300}
.brand-sub{font-size:11px;letter-spacing:.6px;margin-top:4px}
.tagline{position:absolute;left:0;right:0;top:432px;text-align:center;font-size:12.4px;line-height:1.45;color:var(--ink)}
/* symptoms */
.symptoms-title{position:absolute;left:0;right:0;top:17px;text-align:center;color:var(--white);font-size:11.4px}
.symptoms-title::after{content:"";display:block;width:160px;margin:3px auto 0;border-bottom:.6px solid rgba(255,255,255,.8)}
.symptom{position:absolute;left:10px;right:9px;color:var(--white)}
.symptom h3{font-weight:300;font-size:9.4px;display:flex;align-items:center;gap:6px;margin-bottom:2px}
.symptom h3 svg{width:16px;height:16px;flex:none}
.symptom p{font-size:5.9px;line-height:1.45;text-align:justify}
/* programs */
.subhead{position:absolute;left:0;right:0;top:249px;text-align:center;color:var(--rose-text);font-size:6.9px;line-height:1.4}
.benefits{position:absolute;left:17px;top:272px;list-style:none;font-size:7.2px;line-height:1.6;color:var(--ink-soft)}
.benefits li::before{content:"";display:inline-block;width:4px;height:4px;border:.7px solid var(--rose-text);border-radius:50%;margin-right:4px;vertical-align:1px}
</style>
</head>
<body>

<!-- OUTSIDE SPREAD -->
<section class="spread spread--outside">
  <article class="panel">
    <div class="photo" style="top:0;height:200px;background:linear-gradient(180deg,#e9d9c2 0%,#cfbfa8 45%,#8e8f86 62%,#6f5f4e 80%,#4e3d30 100%)" role="img" aria-label="Woman meditating on a wooden dock by a calm mountain lake at sunrise"></div>
    <div style="position:absolute;top:200px;left:0;right:0;height:16px;background:var(--rose-soft)"></div>
    <p class="lead" style="top:208px">Functional medicine's purpose is to heal the physical body in order to engage in our life purpose of connection and emotional and spiritual growth.</p>
    <div class="body" style="top:276px">
      <p>Dr. Elena Sorrel has specialized in women's health for over 25 years. She is an expert in bio-identical hormone replacement therapy (BHRT) and has been a Dermaline BHRT pellet practitioner for over 10 years. Dr. Sorrel also specializes in medical weight loss and has been a practicing functional medicine practitioner through her incorporation of lifestyle change for health optimization throughout her career. Dr. Sorrel has recently expanded her practice to incorporate treatments for adrenal, gastrointestinal and detoxification health issues.</p>
      <p>Dr. Sorrel is a practitioner of the Hale Method of functional medicine. She works in partnership with every patient to develop personalized treatment protocols. She continues to work with her mentor, Dr. Marcus Hale, who has practiced functional medicine for over 25 years.</p>
    </div>
    <div class="footer-band">info@brightpathcorva.com</div>
  </article>

  <article class="panel panel--rose">
    <div class="portrait-ring"><div role="img" aria-label="Smiling family of four sitting together outdoors"></div></div>
    <h2 class="testimonial-title" style="font-weight:300">What do patients' have to say<br>about their experience with Dr. Sorrel</h2>
    <div class="quote-mark" style="top:212px">&#8220;</div>
    <p class="quote" style="top:230px">"What I have loved about being a patient of Dr. Sorrel's over the past five years is her patience and attention to my care and her passion for being on the cutting edge of new medical treatments. I am grateful for her knowledge, skill and expertise." Joanna R.</p>
    <div class="quote-mark" style="top:306px">&#8220;</div>
    <p class="quote" style="top:324px">"Dr Sorrel exudes professionalism and perfectionism… I greatly appreciate these traits. I also feel she is highly skilled, up to date and delivers the Highest Quality of Care. Thanks!" – Dana</p>
    <address class="contact" style="font-style:normal">Bright Path Corva Ridge<br>212 Sage Lane , Corva Ridge, New Mexico<br>Phone: 505-555-0142<br>info@brightpathcorva.com</address>
    <div class="social" aria-label="Social media links"><span></span><span></span><span></span><span></span></div>
    <div class="footer-band"><svg viewBox="0 0 10 10" aria-hidden="true"><circle cx="5" cy="5" r="4.3" fill="none" stroke="#fff" stroke-width=".8"/><path d="M3.4 2.9l1 .9-.5.7c.4.7.9 1.2 1.6 1.6l.7-.5.9 1-.7.7c-1.8-.4-3.3-1.9-3.7-3.7z" fill="#fff"/></svg>505-555-0142</div>
  </article>

  <article class="panel">
    <div class="brand">
      <div class="brand-dot"></div>
      <div class="brand-name">BRIGHT PATH</div>
      <div class="brand-sub">FUNCTIONAL MEDICINE</div>
    </div>
    <div class="photo" style="top:126px;height:271px;background:linear-gradient(180deg,#f3eee8 0%,#e8ddd1 30%,#b59a80 65%,#8c6f55 100%)" role="img" aria-label="Three generations of women walking arm in arm on a beach"></div>
    <h1 class="tagline" style="font-weight:300">Personalized Functional Medicine<br>Specializing in Women's Health</h1>
    <div class="footer-band">www.brightpathcorva.com</div>
  </article>
</section>

<!-- INSIDE SPREAD -->
<section class="spread spread--inside">
  <article class="panel">
    <div class="photo" style="top:0;height:185px;background:linear-gradient(180deg,#c9b9a8 0%,#d8c9b8 45%,#cdb9a0 100%)" role="img" aria-label="Woman in a sun hat sitting on the sand, looking out to sea"></div>
    <div style="position:absolute;left:135px;top:148px;width:72px;height:72px;border-radius:50%;background:var(--paper);padding:3px">
      <div style="width:100%;height:100%;border-radius:50%;background:linear-gradient(180deg,#b8c4cf 0%,#9aa3a8 50%,#6f6a64 100%)" role="img" aria-label="Stacked balancing stones on a pebble beach"></div>
    </div>
    <h2 class="heading" style="top:214px;font-weight:300">Why should you consider<br>a functional medicine visit?</h2>
    <div class="body" style="top:242px"><p>You are tired of feeling tired and overwhelmed. You struggle with foggy thinking and worry that your work performance is suffering. You know you need to get moving, but you're too exhausted to exercise. Your relationship is suffering due to your irritability and lack of libido. Your life goals seem like too much to think about, you just have to get through today.</p></div>
    <h2 class="heading" style="top:347px;font-weight:300">Who else should consider a<br>functional medicine visit?</h2>
    <div class="body" style="top:376px"><p>You want to achieve OPTIMAL health with a personalized medicine approach. You are eating well, exercising and trying to incorporate stress reducing activities such as meditation into your daily routine. You want to know how to minimize the effects of genetics and aging and are ready to take a proactive approach in getting to the highest level of health possible.</p></div>
    <div class="footer-band" style="background:var(--rose-soft)">info@brightpathcorva.com</div>
  </article>

  <article class="panel panel--solid">
    <h2 class="symptoms-title" style="font-weight:300">What Symptoms Do We Treat?</h2>
    <section class="symptom" style="top:54px">
      <h3><svg viewBox="0 0 16 16" aria-hidden="true"><path d="M8 15s-5-5-5-9a5 5 0 0110 0c0 4-5 9-5 9z" fill="#fff"/><circle cx="8" cy="6" r="2" fill="var(--rose)"/></svg>WEIGHT GAIN</h3>
      <p>The major function of cortisol is to help balance blood sugar. When cortisol is out of balance, your body will store body fat rather than burning fat for fuel resulting in weight gain. Menopause results in abdominal weight gain as your body tries to compensate for low estrogen.</p>
    </section>
    <section class="symptom" style="top:132px">
      <h3><svg viewBox="0 0 16 16" aria-hidden="true"><rect x="1" y="4" width="12" height="8" rx="1" fill="none" stroke="#fff" stroke-width="1.2"/><rect x="13" y="6.5" width="2" height="3" fill="#fff"/><rect x="2.5" y="5.5" width="3" height="5" fill="#fff"/></svg>FATIGUE</h3>
      <p>Adrenal exhaustion is the result of long-term stress that depletes cortisol. Testing and correcting cortisol will improve energy levels. Stress can also result in mitochondrial dysfunction. Organic acid testing can tell us what is needed to support your mitochondria to increase energy production.</p>
    </section>
    <section class="symptom" style="top:212px">
      <h3><svg viewBox="0 0 16 16" aria-hidden="true"><circle cx="8" cy="8" r="6.5" fill="none" stroke="#fff" stroke-width="1.2"/><path d="M8 2v12M2 8h12" stroke="#fff" stroke-width=".8"/></svg>DEPRESSION</h3>
      <p>Our focus on treating anxiety and depression by treating imbalance in hormone levels, cortisol and the brain neurotransmitters dopamine, epinephrine and norepinephrine can help support optimization of mood and energy.</p>
    </section>
    <section class="symptom" style="top:287px">
      <h3><svg viewBox="0 0 16 16" aria-hidden="true"><path d="M8 14C4 12 1 9 2 4c3 0 5 2 6 5 1-3 3-5 6-5 1 5-2 8-6 10z" fill="#fff"/></svg>FEMALE HORMONE IMBALANCE</h3>
      <p>Bio-identical hormone pellet therapy is our specialty. We work to optimize hormone levels with bio-identical hormones, but also know that adrenal protocols can improve symptoms of hot flashes, nights sweats, and foggy thinking. Properly balanced hormones help you look and feel younger. Women experience improved skin elasticity, sleep quality, and libido as a consequence of hormonal balance.</p>
    </section>
    <section class="symptom" style="top:390px">
      <h3><svg viewBox="0 0 16 16" aria-hidden="true"><path d="M8 14S1 9.5 1 5.3A3.3 3.3 0 018 4a3.3 3.3 0 017 1.3C15 9.5 8 14 8 14z" fill="none" stroke="#fff" stroke-width="1.1"/><path d="M3 8h2.5l1-2 1.5 4 1-2H13" fill="none" stroke="#fff" stroke-width=".9"/></svg>GI PROBLEMS</h3>
      <p>The immune cells that line our digestive tract are regulated by cortisol. Cortisol imbalance results in inflammation and "leaky gut" causing digestive symptoms like bloating, heartburn, constipation, or diarrhea. Utilizing a comprehensive program that includes avoiding inflammatory foods and stool testing allow us to find underlying infection and sources of inflammation.</p>
    </section>
    <div class="footer-band" style="background:var(--rose-soft)"><svg viewBox="0 0 10 10" aria-hidden="true"><circle cx="5" cy="5" r="4.3" fill="none" stroke="#fff" stroke-width=".8"/><path d="M3.4 2.9l1 .9-.5.7c.4.7.9 1.2 1.6 1.6l.7-.5.9 1-.7.7c-1.8-.4-3.3-1.9-3.7-3.7z" fill="#fff"/></svg>505-555-0142</div>
  </article>

  <article class="panel">
    <h2 class="heading heading--rule" style="top:25px;font-weight:300">What can I expect from my first visit?</h2>
    <div class="body" style="top:45px"><p>During your initial consultation, we will get to know each other and begin to design your personalized health program based on your goals. Together, we will explore your health history and symptoms as well as lifestyle factors such as diet and sleep. We will discuss your goals and reasons for getting healthy. We incorporate lifestyle changes including stress reduction, diet and exercise in all programs for healing. We will discuss the variety of tests available including blood work, hormone testing, cortisol, GI, and organic acid tests as well as nutritional and personal coaching options.</p></div>
    <h2 class="heading heading--rule" style="top:156px;font-weight:300">Our Programs</h2>
    <div class="body" style="top:176px"><p>Our goal is to optimize your health so that you feel fabulous virtually every day. Treatment protocols are a combination of supplement support and hormone balance in addition to lifestyle programs. We will work together to determine what type of treatment program works best for you.</p></div>
    <p class="subhead">Enjoy the Benefits of Health and Hormonal<br>Balance with Functional Medicine</p>
    <ul class="benefits">
      <li>Look and Feel Younger</li>
      <li>Feel Happy and Energized</li>
      <li>Improve Sleep and Mental Clarity</li>
      <li>Restore Sexual Desire</li>
      <li>…And Much More</li>
    </ul>
    <div class="photo" style="top:344px;height:163px;background:linear-gradient(120deg,#dfe3e6 0%,#c9ccce 40%,#9aa1ab 70%,#6e7686 100%)" role="img" aria-label="Smiling older couple holding hands by a bright window"></div>
    <div class="footer-band footer-band--overlay">www.brightpathcorva.com</div>
  </article>
</section>

</body>
</html>
```